R&D and Engineering Management Consultancy Needs Branding

I need a branding style for my consultancy - specifically I need business cards by Tuesday 26 April (9 days away!) to take to a conference, including a logo design. If this service does not include printing I will need it in time for printing.

Later, the same logo and style needs to be incorporated into a Powerpoint template and a Word Template. Optionally also a Pages template.

The branding image needs to project and/or support the following qualities:
High tech
Speed and throughput
Lean
Innovation
Dependability
Quality

One possible concept is based on the Principal’s surname – Marrowby, which is a small bird. So a logo design which is a stylized rendition of a bird may work well. Flight implies speed, and the style would be “techy”, perhaps geometric in a way that conveys Lean – boiling things down to the essential elements.

Other concepts are welcome.
You can find me on https://au.peoplenexa.com/in/hollismarrowby

Business Card Information
Marrowby Consulting
Hollis Marrowby
BE (Hons), CSM, CSPO, SA
Principal Consultant
Mobile: +61 (0)455 913 607
Email: hollis@marrowbyconsulting.com
Web: www.marrowbyconsulting.com

Reverse:
Lean/Agile Software Development at Scale
Lean Product Development
Lean Portfolio Management
Organisational development and transformation
Mentoring and coaching of Technical Leaders
Program and project management
Business Processes and Systems

Target Market(s)

The target market for this consultancy comprises technology-based product and/or services development companies. They typically engage in one or a mix of software, electronics, mechanical, ASIC and MEMS development activities. They range from small startups to transnational corporations staffed by highly skilled engineers, developers and scientists. The consultancy is applicable across a range of domains such as biomedical device development, inkjet printing technology, telecommunications, internet and mesh networking technologies, renewable energy systems, and electronic product development of all kinds.

Industry/Entity Type

Information Technology

Contact Information for Business Card

Marrowby Consulting
Hollis Marrowby
BE (Hons), CSM, CSPO, SA
Principal Consulting

Reverse:
➢ Lean/Agile Software Development
➢ Lean Product Development
➢ Lean Portfolio Management
➢ Organisational development and transformation
➢ Mentoring and coaching of Technical Leaders
➢ Program and project management
➢ Business Processes and Systems

Logo Text

Just graphical

Font styles to use
Sans Serif

Requirements
Must have
• A clean professional look
Nice to have
• Use a bird motif based on my name Marrowby
• The bird's colours are yellow/gold, light brown, black and red so these suggest a colour scheme.
• I have uploaded a stylised bird design that I like but this belongs to another company. A variation on this might be good.
Should not have
• Too much clutter. If the details are too much to fit, drop the qualifications line

```html
<!DOCTYPE html>
<html lang="en">
<head>
<meta charset="utf-8">
<title>Marrowby Consulting – Business Cards</title>
<link rel="stylesheet" href="https://fonts.googleapis.com/css2?family=Open+Sans:wght@300;400;600;700&display=swap">
<style>
  :root {
    --bg: #3a2f3a;
    --teal-dark: #073b37;
    --teal: #0a4f49;
    --teal-light: #0d5a53;
    --yellow: #ffff1f;
    --lime-line: #8fae3a;
    --white: #ffffff;
    --card-w: 560px;
    --card-h: 342px;
  }
  * { box-sizing: border-box; margin: 0; padding: 0; }
  html, body { width: 1200px; height: 800px; overflow: hidden; }
  body {
    background: var(--bg);
    font-family: "Open Sans", sans-serif;
    display: flex;
    align-items: center;
    justify-content: center;
    gap: 30px;
  }
  .card {
    position: relative;
    width: var(--card-w);
    height: var(--card-h);
    background: linear-gradient(135deg, var(--teal-dark) 0%, var(--teal) 55%, var(--teal-light) 100%);
    overflow: hidden;
    color: var(--white);
  }

  /* Front */
  .front .band {
    position: absolute; left: 0; right: 0; bottom: 0; height: 46px;
    background: var(--yellow);
  }
  .front .brand {
    position: absolute; left: 24px; top: 70px; width: 270px;
    display: flex; flex-direction: column; align-items: center;
  }
  .front .brand-mark {
    width: 110px; height: 110px; border-radius: 50%;
    border: 3px solid var(--yellow);
    margin-bottom: 18px;
  }
  .front .brand-name {
    color: var(--yellow); font-weight: 600; font-size: 26px; white-space: nowrap;
  }
  .front .web {
    position: absolute; left: 24px; width: 270px; bottom: 58px;
    text-align: center; font-size: 11px; color: var(--yellow);
  }
  .front .divider {
    position: absolute; left: 306px; top: 40px; width: 1px; height: 230px;
    background: var(--lime-line);
  }
  .front .contact {
    position: absolute; left: 330px; top: 92px; right: 16px;
  }
  .front .person {
    color: var(--yellow); font-weight: 700; font-size: 21px; margin-bottom: 6px; white-space: nowrap;
  }
  .front .cred, .front .role { font-size: 14px; line-height: 1.45; white-space: nowrap; }
  .front .lines { margin-top: 22px; font-size: 13px; line-height: 1.7; white-space: nowrap; }

  /* Back */
  .back .band {
    position: absolute; left: 0; right: 0; bottom: 32px; height: 48px;
    background: var(--yellow);
  }
  .back .heading {
    position: absolute; right: 40px; top: 40px;
    color: var(--yellow); font-size: 20px; font-weight: 400; white-space: nowrap;
  }
  .services {
    list-style: none; position: absolute;
    font-size: 11px; font-weight: 600; white-space: nowrap;
  }
  .services li { position: relative; padding-left: 16px; line-height: 22px; height: 22px; }
  .services li::before {
    content: ""; position: absolute; left: 0; top: 8px;
    width: 6px; height: 6px;
    border-radius: 50%; background: var(--white);
  }
  .services.left { left: 34px; top: 74px; }
  .services.right { left: 262px; top: 184px; }
</style>
</head>
<body>
  <section class="card front" aria-label="Business card front">
    <div class="brand">
      <div class="brand-mark"></div>
      <div class="brand-name">Marrowby Consulting</div>
    </div>
    <div class="web">www.marrowbyconsulting.com</div>
    <div class="divider"></div>
    <div class="contact">
      <div class="person">Hollis Marrowby</div>
      <div class="cred">BE (Hons), CSM, CSPO, SA</div>
      <div class="role">Principal Consulting</div>
      <div class="lines">
        <div>: +61 (0)455 913 607</div>
        <div>: hollis@marrowbyconsulting.com</div>
      </div>
    </div>
    <div class="band"></div>
  </section>

  <section class="card back" aria-label="Business card back">
    <h2 class="heading">consulting services in :-</h2>
    <ul class="services left">
      <li>Lean Product Development</li>
      <li>Lean Portfolio Management</li>
      <li>Lean/Agile Software Development</li>
      <li>Organisational development and transformation</li>
    </ul>
    <ul class="services right">
      <li>Program and project management</li>
      <li>Business Processes and Systems</li>
      <li>Mentoring and coaching of Technical Leaders</li>
    </ul>
    <div class="band"></div>
  </section>
</body>
</html>
```